Values Statement poster template

We want to develop a poster template for our company policies and statements which promote our company values in our workplaces.
These documents are important in showing our clients, suppliers and employees who we are and what we stand for.
The graphic design will incorporate our company logo, and be bright, uplifting and inspiring, developing a graphic theme that we can utilise for other company documents. The design will graphically illustrate and support our values statement, with colour and modern design.
This values poster will be the first in a series of documents using the same theme.The format will be a4 and a3 portrait
We are an environmental service business specialising in rehabilitation and revegetation

Target Market(s)

Tier one clients in industry, Mining, Construction and agriculture

Font styles to use
Other font styles liked:
• calibri

Requirements
Must have
• Professional , high end feel, able to read clearly on a poster
Nice to have
• graphic design elements, symbols, etc which support the message, that can be carried through to various documents such as quality, environmental, safety policies
A bright theme which ties in with our logo colours.

```html
<!DOCTYPE html>
<html lang="en">
<head>
<meta charset="utf-8">
<title>Our Values – Verdanta</title>
<link href="https://fonts.googleapis.com/css2?family=Paytone+One&family=Questrial&display=swap" rel="stylesheet">
<style>
  :root {
    --stage: #2c2c2c;
    --paper: #ebebeb;
    --panel: #ffffff;
    --banner: #8c8c8c;
    --ink: #2a2a2a;
    --muted: #555555;
    --green: #5bbb12;
    --blue: #2a6ee0;
    --orange: #f06a1c;
    --forest: #0b6b33;
    --cyan: #12a9cc;
    --yellow: #f5b800;
    --magenta: #c82fd8;
    --brand: #17773a;
  }
  html, body {
    margin: 0;
    width: 1200px;
    height: 861px;
    overflow: hidden;
    background: var(--stage);
  }
  .poster {
    position: absolute;
    top: 57px;
    width: 529px;
    height: 747px;
    display: block;
  }
  .poster--numbered { left: 49px; }
  .poster--iconic { left: 616px; }
  .defs-holder { position: absolute; width: 0; height: 0; }

  .paper { fill: var(--paper); }
  .panel { fill: var(--panel); }
  .banner { fill: var(--banner); }
  .banner-title { font-family: "Paytone One", sans-serif; font-size: 64px; fill: #fff; letter-spacing: 1px; }
  .value-title { font-family: "Paytone One", sans-serif; font-size: 29px; }
  .value-sub { font-family: "Questrial", sans-serif; font-style: italic; font-size: 18px; fill: var(--muted); }
  .value-lead { font-family: "Questrial", sans-serif; font-weight: 700; font-size: 12.5px; fill: var(--ink); }
  .value-body { font-family: "Questrial", sans-serif; font-size: 12px; fill: var(--ink); }
  .value-italic { font-family: "Questrial", sans-serif; font-style: italic; font-size: 11.5px; fill: var(--ink); }
  .end { text-anchor: end; }
  .t-green { fill: var(--green); }
  .t-blue { fill: var(--blue); }
  .t-orange { fill: var(--orange); }
  .t-forest { fill: var(--forest); }
  .t-cyan { fill: var(--cyan); }
  .t-yellow { fill: var(--yellow); }
  .t-magenta { fill: var(--magenta); }
  .value-number { font-family: "Paytone One", sans-serif; font-size: 76px; text-anchor: middle; }
  .brand-name { font-family: "Questrial", sans-serif; font-size: 62px; fill: var(--brand); }
  .brand-dot { fill: var(--orange); }
</style>
</head>
<body>

<svg class="defs-holder" aria-hidden="true">
  <defs>
    <linearGradient id="grad-green" x1="0" y1="0" x2="0" y2="1"><stop offset="0" stop-color="#a6ec55"/><stop offset="1" stop-color="#47ad15"/></linearGradient>
    <linearGradient id="grad-blue" x1="0" y1="0" x2="0" y2="1"><stop offset="0" stop-color="#5ea6ff"/><stop offset="1" stop-color="#1850c4"/></linearGradient>
    <linearGradient id="grad-orange" x1="0" y1="0" x2="0" y2="1"><stop offset="0" stop-color="#ffa466"/><stop offset="1" stop-color="#de601a"/></linearGradient>
    <linearGradient id="grad-forest" x1="0" y1="0" x2="0" y2="1"><stop offset="0" stop-color="#1fd372"/><stop offset="1" stop-color="#0a7538"/></linearGradient>
    <linearGradient id="grad-cyan" x1="0" y1="0" x2="0" y2="1"><stop offset="0" stop-color="#22e0f8"/><stop offset="1" stop-color="#0a90b2"/></linearGradient>
    <linearGradient id="grad-yellow" x1="0" y1="0" x2="0" y2="1"><stop offset="0" stop-color="#ffd52e"/><stop offset="1" stop-color="#dca406"/></linearGradient>
    <linearGradient id="grad-magenta" x1="0" y1="0" x2="0" y2="1"><stop offset="0" stop-color="#e760f3"/><stop offset="1" stop-color="#b014c4"/></linearGradient>

    <symbol id="values-layout" viewBox="0 0 999 1413">
      <rect class="paper" width="999" height="1413"/>

      <!-- heading banner -->
      <polygon class="banner" points="0,83 422,83 460,150 422,220 0,220"/>
      <text class="banner-title" x="38" y="168">OUR VALUES</text>

      <!-- left-facing values: 2, 4, 6 -->
      <g class="value value--2">
        <polygon fill="url(#grad-blue)" points="277,316 455,316 535,456 455,596 277,596"/>
        <polygon class="panel" points="0,344 438,344 504,457 438,570 0,570"/>
      </g>
      <g class="value value--4">
        <polygon fill="url(#grad-forest)" points="277,605 455,605 535,745 455,885 277,885"/>
        <polygon class="panel" points="0,633 438,633 504,746 438,859 0,859"/>
      </g>
      <g class="value value--6">
        <polygon fill="url(#grad-yellow)" points="277,894 455,894 535,1034 455,1174 277,1174"/>
        <polygon class="panel" points="0,922 438,922 504,1035 438,1148 0,1148"/>
      </g>

      <!-- right-facing values: 1, 3, 5, 7 -->
      <g class="value value--1">
        <polygon fill="url(#grad-green)" points="542,173 717,173 717,451 542,451 462,312"/>
        <polygon class="panel" points="566,197 999,197 999,424 566,424 502,311"/>
      </g>
      <g class="value value--3">
        <polygon fill="url(#grad-orange)" points="542,462 717,462 717,740 542,740 462,601"/>
        <polygon class="panel" points="566,486 999,486 999,713 566,713 502,600"/>
      </g>
      <g class="value value--5">
        <polygon fill="url(#grad-cyan)" points="542,751 717,751 717,1029 542,1029 462,890"/>
        <polygon class="panel" points="566,775 999,775 999,1002 566,1002 502,889"/>
      </g>
      <g class="value value--7">
        <polygon fill="url(#grad-magenta)" points="542,1040 717,1040 717,1318 542,1318 462,1179"/>
        <polygon class="panel" points="566,1064 999,1064 999,1291 566,1291 502,1178"/>
      </g>

      <!-- value 1 -->
      <text class="value-title t-green" x="617" y="249">WE VALUE OUR PEOPLE</text>
      <text class="value-sub" x="619" y="266">above everything else</text>
      <text class="value-lead" x="620" y="287">WE DEMONSTRATE THIS BY:</text>
      <text class="value-body" x="620" y="306">Providing safe, positive, enjoyable workplaces where everyone</text>
      <text class="value-body" x="620" y="317">feels valued and respected</text>
      <text class="value-body" x="620" y="335">Providing Careers, not Jobs, we grow together</text>
      <text class="value-body" x="620" y="355">Encouraging inclusion, participation and collaboration</text>
      <text class="value-body" x="620" y="375">Recognising and rewarding contribution and excellence</text>
      <text class="value-body" x="620" y="395">Supporting our people through tough times</text>

      <!-- value 2 -->
      <text class="value-title t-blue end" x="386" y="410">WE ARE PROUD OF</text>
      <text class="value-title t-blue end" x="386" y="432">WHO WE ARE</text>
      <text class="value-lead end" x="384" y="452">OUR REPUTATION MEANS THE WORLD TO US. WE:</text>
      <text class="value-body end" x="383" y="470">Treat everyone with respect and we expect it in return</text>
      <text class="value-body end" x="380" y="486">Follow the rules</text>
      <text class="value-body end" x="380" y="502">Do what we say we will do</text>
      <text class="value-body end" x="380" y="520">Own our mistakes and we fix them</text>
      <text class="value-body end" x="379" y="539">Are trustworthy and transparent</text>

      <!-- value 3 -->
      <text class="value-title t-orange" x="617" y="555">WE DO GOOD THINGS</text>
      <text class="value-sub" x="619" y="572">for the planet</text>
      <text class="value-body" x="620" y="596">Our products are helping revegetate Australia, which we are</text>
      <text class="value-body" x="620" y="615">tremendously proud of.</text>
      <text class="value-body" x="620" y="634">We minimise our environmental impact in everything we do.</text>

      <!-- value 4 -->
      <text class="value-title t-forest end" x="386" y="691">WE SUCCEED TOGETHER</text>
      <text class="value-lead end" x="384" y="706">WE BELIEVE IN WIN-WIN RELATIONSHIPS. WHEN OUR</text>
      <text class="value-lead end" x="384" y="719">BUSINESS IS PROFITABLE EVERYONE BENEFITS, OUR</text>
      <text class="value-lead end" x="384" y="732">OWNERS, EMPLOYEES, CLIENTS AND THE COMMUNITY.</text>
      <text class="value-lead end" x="384" y="745">AT VERDANTA WE:</text>
      <text class="value-body end" x="379" y="762">Work as a team, we get it done together</text>
      <text class="value-body end" x="379" y="778">We treat our suppliers and subcontractors like they are</text>
      <text class="value-body end" x="379" y="788">part of the team</text>
      <text class="value-body end" x="379" y="805">Are building on our success, and growing together</text>
      <text class="value-body end" x="379" y="823">Choose to work with employees, customers and suppliers</text>
      <text class="value-body end" x="379" y="833">who fit our values</text>

      <!-- value 5 -->
      <text class="value-title t-cyan" x="617" y="848">WE SET THE STANDARD</text>
      <text class="value-body" x="620" y="867">We are uncompromising on quality</text>
      <text class="value-body" x="620" y="889">We are the best at what we do, and we do what we are</text>
      <text class="value-body" x="620" y="900">best at</text>
      <text class="value-body" x="620" y="920">We are always improving</text>
      <text class="value-body" x="620" y="943">We are pioneering</text>

      <!-- value 6 -->
      <text class="value-title t-yellow end" x="382" y="991">WE GIVE BACK</text>
      <text class="value-body end" x="379" y="1024">We appreciate our success and we give back by</text>
      <text class="value-body end" x="379" y="1046">supporting our community, and those less fortunate.</text>

      <!-- value 7 -->
      <text class="value-title t-magenta" x="617" y="1115">OUR WORKPLACES</text>
      <text class="value-title t-magenta" x="617" y="1137">ARE SAFE</text>
      <text class="value-italic" x="616" y="1152">There is nothing more important to us than our people going home</text>
      <text class="value-italic" x="616" y="1165">healthy and safe every day. We won’t accept anything less. We believe</text>
      <text class="value-italic" x="616" y="1177">safety is a management choice. By providing safe work systems, and</text>
      <text class="value-italic" x="616" y="1190">education we achieve our daily goal of Zero Harm. At Verdanta we;</text>
      <text class="value-body" x="616" y="1201">Take the time to make our work areas safe, whatever it takes</text>
      <text class="value-body" x="616" y="1215">Don’t accept shortcuts</text>
      <text class="value-body" x="616" y="1228">Look out for each other</text>
      <text class="value-body" x="616" y="1241">Investigate our incidents and learn from them, we won’t accept repeats</text>
      <text class="value-body" x="616" y="1254">Are constantly looking for ways to improve the safety of our workplaces.</text>
      <text class="value-body" x="616" y="1267">Think safe, work safer, go home safe!</text>

      <!-- brand name -->
      <circle class="brand-dot" cx="112" cy="1270" r="26"/>
      <text class="brand-name" x="160" y="1292">Verdanta</text>
    </symbol>
  </defs>
</svg>

<!-- Variant A: numbered markers -->
<svg class="poster poster--numbered" viewBox="0 0 999 1413" role="img" aria-label="Our Values poster with numbered values">
  <use href="#values-layout"/>
  <g class="markers">
    <text class="value-number t-green" x="565" y="333">1</text>
    <text class="value-number t-blue" x="438" y="484">2</text>
    <text class="value-number t-orange" x="570" y="625">3</text>
    <text class="value-number t-forest" x="437" y="773">4</text>
    <text class="value-number t-cyan" x="565" y="916">5</text>
    <text class="value-number t-yellow" x="437" y="1059">6</text>
    <text class="value-number t-magenta" x="563" y="1203">7</text>
  </g>
</svg>

<!-- Variant B: icon markers -->
<svg class="poster poster--iconic" viewBox="0 0 999 1413" role="img" aria-label="Our Values poster with icons for each value">
  <use href="#values-layout"/>
  <g class="markers">
    <path class="icon-heart" d="M566 340 C528 312 520 288 536 274 C548 264 562 272 566 284 C570 272 584 264 596 274 C612 288 604 312 566 340Z" fill="none" stroke="var(--green)" stroke-width="7"/>

    <g class="icon-rosette">
      <polygon points="416,462 402,490 416,486 424,498 436,470" fill="var(--blue)"/>
      <polygon points="458,462 472,490 458,486 450,498 438,470" fill="var(--blue)"/>
      <circle cx="437" cy="448" r="30" fill="var(--blue)"/>
      <circle cx="437" cy="448" r="19" fill="#fff"/>
      <polygon points="437,434 441,444 451,448 441,452 437,462 433,452 423,448 433,444" fill="var(--blue)"/>
    </g>

    <g class="icon-globe" fill="none" stroke="var(--orange)" stroke-width="5">
      <circle cx="570" cy="598" r="31"/>
      <ellipse cx="570" cy="598" rx="13" ry="31"/>
      <line x1="539" y1="598" x2="601" y2="598"/>
    </g>

    <rect x="402" y="716" width="72" height="64" rx="12" fill="var(--forest)" role="img" aria-label="Icon: two team members giving a high five"/>

    <polygon class="icon-star" points="565,858 574,880 598,882 580,897 586,921 565,908 544,921 550,897 532,882 556,880" fill="var(--cyan)"/>

    <rect x="404" y="998" width="66" height="68" rx="12" fill="var(--yellow)" role="img" aria-label="Icon: two open helping hands"/>

    <g class="icon-shield">
      <circle cx="563" cy="1180" r="34" fill="var(--magenta)"/>
      <path d="M563 1156 L583 1163 L583 1180 C583 1193 574 1201 563 1205 C552 1201 543 1193 543 1180 L543 1163 Z" fill="#fff"/>
      <polyline points="553,1180 560,1188 574,1172" fill="none" stroke="var(--magenta)" stroke-width="5" stroke-linecap="round" stroke-linejoin="round"/>
    </g>
  </g>
</svg>

</body>
</html>
```